Brenton Civil

We need a Standard Professional Company Letterhead, company standard document template, coversheet template for a civil construction company. We would like the designs to use the company colour red

I have attached existing templates that need to improve greatly but please use as a quide of general layout.

```html
<!DOCTYPE html>
<html lang="en">
<head>
<meta charset="utf-8">
<title>Brenton Civil Letterhead</title>
<link rel="stylesheet" href="https://fonts.googleapis.com/css2?family=Open+Sans:wght@400;600&family=Roboto:wght@500&display=swap">
<style>
  :root {
    --brand-red: #c01f2f;
    --ink: #1f1f1f;
    --body-text: #4a4a4a;
    --footer-grey: #b9b9bd;
    --paper: #ffffff;
    --signature-tone: #ececec;
  }
  * { box-sizing: border-box; margin: 0; padding: 0; }
  html, body { width: 1063px; height: 1200px; overflow: hidden; background: var(--paper); }
  .letterhead {
    position: relative;
    width: 1063px;
    height: 1200px;
    background: linear-gradient(180deg, #ffffff 0%, #f7f7f8 100%);
    font-family: "Open Sans", sans-serif;
    color: var(--body-text);
  }
  .brand {
    position: absolute;
    left: 90px;
    top: 110px;
    display: flex;
    align-items: center;
    gap: 18px;
  }
  .brand-dot {
    width: 74px;
    height: 74px;
    border-radius: 50%;
    background: var(--brand-red);
  }
  .brand-name {
    font-family: "Open Sans", sans-serif;
    font-weight: 600;
    font-size: 21px;
    line-height: 1.15;
    letter-spacing: 1px;
    color: var(--brand-red);
  }
  .contact {
    position: absolute;
    right: 90px;
    top: 86px;
    font-size: 13px;
    line-height: 19px;
    color: var(--ink);
  }
  .contact-line { display: flex; align-items: center; gap: 7px; }
  .contact-line svg { width: 12px; height: 12px; flex: none; }
  .contact-address { margin-bottom: 2px; }
  .letter-body {
    position: absolute;
    left: 110px;
    top: 270px;
    width: 780px;
    font-size: 14.5px;
    line-height: 22px;
  }
  .salutation { margin-bottom: 14px; }
  .letter-body p.paragraph { margin-bottom: 22px; }
  .closing { margin-top: 6px; }
  .signature-area {
    margin-top: 16px;
    width: 140px;
    height: 80px;
    background: var(--signature-tone);
    border-radius: 4px;
  }
  .footer {
    position: absolute;
    left: 0;
    bottom: 0;
    width: 1063px;
    height: 96px;
  }
  .footer svg { display: block; }
  .abn {
    position: absolute;
    right: 48px;
    bottom: 44px;
    font-family: "Roboto", sans-serif;
    font-weight: 500;
    font-size: 16px;
    color: #ffffff;
    letter-spacing: 0.3px;
  }
</style>
</head>
<body>
<main class="letterhead">
  <header>
    <div class="brand">
      <div class="brand-dot"></div>
      <div class="brand-name">BRENTON<br>CIVIL PTY LTD</div>
    </div>
    <address class="contact" style="font-style:normal">
      <div class="contact-address">PO Box 412 , Ridgeview Qld 4790</div>
      <div class="contact-line">
        <svg viewBox="0 0 12 12"><rect x="3" y="0.8" width="6" height="10.4" rx="1.2" fill="none" stroke="var(--brand-red)" stroke-width="1.3"/><circle cx="6" cy="9.3" r="0.7" fill="var(--brand-red)"/></svg>
        <span>0400 555 018</span>
      </div>
      <div class="contact-line">
        <svg viewBox="0 0 12 12"><rect x="0.8" y="2.3" width="10.4" height="7.4" rx="0.8" fill="none" stroke="var(--brand-red)" stroke-width="1.3"/><path d="M1 3l5 4 5-4" fill="none" stroke="var(--brand-red)" stroke-width="1.3"/></svg>
        <span>office@brentoncivil.com.au</span>
      </div>
      <div class="contact-line">
        <svg viewBox="0 0 12 12"><circle cx="6" cy="6" r="5" fill="none" stroke="var(--brand-red)" stroke-width="1.3"/><path d="M1 6h10M6 1c-2.4 2.8-2.4 7.2 0 10M6 1c2.4 2.8 2.4 7.2 0 10" fill="none" stroke="var(--brand-red)" stroke-width="1"/></svg>
        <span>www.brentoncivil.com.au</span>
      </div>
    </address>
  </header>

  <section class="letter-body">
    <p class="salutation">Dear customer,</p>
    <p class="paragraph">Lorem ipsum dolor sit amet, consectetur adipisicing elit, sed do eiusmod tempor incididunt ut labore et dolore magna aliqua. Ut enim ad minim veniam, quis nostrud exercitation ullamco laboris nisi ut aliquip ex ea commodo consequat. Duis aute irure dolor in reprehenderit in voluptate velit esse cillum dolore eu fugiat nulla pariatur. Excepteur sint occaecat cupidatat non proident, sunt in culpa qui officia deserunt mollit anim id est laborum.</p>
    <p class="paragraph">Lorem ipsum dolor sit amet, consectetur adipisicing elit, sed do eiusmod tempor incididunt ut labore et dolore magna aliqua. Ut enim ad minim veniam, quis nostrud exercitation ullamco laboris nisi ut aliquip ex ea commodo consequat. Duis aute irure dolor in reprehenderit in voluptate velit esse cillum dolore eu fugiat nulla pariatur. Excepteur sint occaecat cupidatat non proident, sunt in culpa qui officia deserunt mollit anim id est laborum.</p>
    <p class="paragraph">Lorem ipsum dolor sit amet, consectetur adipisicing elit, sed do eiusmod tempor incididunt ut labore et dolore magna aliqua. Ut enim ad minim veniam, quis nostrud exercitation ullamco laboris nisi ut aliquip ex ea commodo consequat. Duis aute irure dolor in reprehenderit in voluptate velit esse cillum dolore eu fugiat nulla pariatur. Excepteur sint occaecat cupidatat non proident, sunt in culpa qui officia deserunt mollit anim id est laborum.</p>
    <p class="paragraph">Lorem ipsum dolor sit amet, consectetur adipisicing elit, sed do eiusmod tempor incididunt ut labore et dolore magna aliqua. Ut enim ad minim veniam, quis nostrud exercitation ullamco laboris nisi ut aliquip ex ea commodo consequat. Duis aute irure dolor in reprehenderit.</p>
    <p class="closing">Yours Sincerely,</p>
    <div class="signature-area" role="img" aria-label="Handwritten signature of the sender"></div>
  </section>

  <footer class="footer">
    <svg width="1063" height="96" viewBox="0 0 1063 96">
      <path d="M0 54 H706 C722 54 728 48 733 40 L742 40 C736 52 731 60 716 60 H0 Z" fill="var(--footer-grey)"/>
      <path d="M0 64 H716 C734 64 739 56 745 44 C751 31 761 24 782 24 H1063 V96 H0 Z" fill="var(--brand-red)"/>
    </svg>
    <div class="abn">ABN : 12 345 678 901</div>
  </footer>
</main>
</body>
</html>
```